Football blog needs a Wordpress design new site

We need a wordpress design for a new football blog site. We would like to see a design that uses the colours green, white and black and one that makes good use of the slideshow widgets as scene in the site 'www.trenvix.net'
We would like a modern and sleek looking site but one that is also professional and easy to navigate.
Unfortunately due to unforeseen circumstances we are having to shorten the deadline date for this project.
The new deadline date is 16/07/2014.
We apologise for any inconveniance
It Professional

```html
<!DOCTYPE html>
<html lang="en">
<head>
<meta charset="utf-8">
<title>Sideline Chatter – Football Blog</title>
<link href="https://fonts.googleapis.com/css2?family=Open+Sans:wght@400;600;700&display=swap" rel="stylesheet">
<style>
:root{
  --green:#1e9a3a;
  --black:#1c1c1c;
  --footer:#222;
  --footer-bar:#111;
  --text:#555;
  --muted:#999;
  --line:#e4e4e4;
  --white:#fff;
  --bg:#f4f4f4;
}
*{box-sizing:border-box;margin:0;padding:0}
html,body{width:756px;height:1200px;overflow:hidden}
body{font-family:"Open Sans",Arial,sans-serif;color:var(--text);background:var(--white);font-size:7px;line-height:1.45;position:relative}
a{color:inherit;text-decoration:none}

/* header */
.site-header{height:76px;position:relative}
.brand{position:absolute;left:30px;top:10px;display:flex;align-items:center;gap:6px}
.brand-dot{width:20px;height:20px;border-radius:50%;background:var(--green)}
.brand-name{font-size:16px;font-weight:700;color:var(--green)}
.follow{position:absolute;right:30px;top:8px;display:flex;align-items:center;gap:5px;font-size:7.5px;color:var(--black)}
.follow .ico{width:10px;height:10px;border-radius:50%;background:var(--black)}
.follow .ico.g{background:var(--green)}
.nav{position:absolute;right:30px;top:42px;display:flex;gap:4px;font-size:8px;font-weight:600;color:var(--black)}
.nav a{padding:5px 10px;border-radius:2px}
.nav a.active{background:var(--green);color:var(--white)}
.nav .caret{font-size:5.5px;color:var(--muted)}

/* slider */
.slider{height:186px;display:grid;grid-template-columns:110px 150px 236px 130px 130px;grid-template-rows:1fr 1fr;gap:2px;background:var(--black)}
.tile{position:relative;overflow:hidden}
.tile.big{grid-row:span 2;grid-column:3;grid-row-start:1}
.tile .fill{position:absolute;inset:0}
.tile .caption{position:absolute;left:7px;right:5px;bottom:6px;color:var(--white)}
.tag-label{display:inline-block;background:var(--green);color:var(--white);font-size:5.5px;font-weight:700;padding:1px 4px;text-transform:uppercase;margin-bottom:2px}
.tile .caption h3{font-size:8px;font-weight:700;line-height:1.2;text-shadow:0 1px 2px rgba(0,0,0,.6)}
.tile.big .caption h3{font-size:11px}
.slider-band{height:6px;background:var(--green)}

/* content */
.content{display:flex;gap:26px;padding:18px 30px 0}
.posts{width:486px}
.post{display:flex;gap:16px;height:168px;border-bottom:1px solid var(--line);padding-top:6px}
.post:last-of-type{border-bottom:none;height:150px}
.post .thumb{width:108px;height:98px;flex:none;border-radius:2px}
.post h2{font-size:10.5px;font-weight:600;color:var(--black);margin-bottom:4px}
.meta{display:flex;gap:9px;font-size:6.5px;color:var(--muted);margin-bottom:6px;align-items:center}
.meta i{display:inline-block;width:6px;height:6px;background:var(--green);border-radius:1px;margin-right:2px;vertical-align:-1px}
.post p{font-size:7px;margin-bottom:4px}
.read-more{font-size:6.5px;color:var(--green);font-weight:600}

.pagination{display:flex;justify-content:center;gap:3px}
.pagination a{min-width:18px;height:16px;border:1px solid var(--line);font-size:7px;display:flex;align-items:center;justify-content:center;padding:0 4px;color:var(--text)}
.pagination a.current{background:var(--green);color:var(--white);border-color:var(--green)}

/* sidebar */
.sidebar{width:184px}
.widget{margin-bottom:14px}
.widget h4{font-size:10px;font-weight:600;color:var(--black);padding-bottom:4px;border-bottom:2px solid var(--green);margin-bottom:6px}
.cat-list li{list-style:none;font-size:7px;padding:4px 0;border-bottom:1px solid var(--line);display:flex;gap:5px;align-items:center}
.cat-list li::before{content:"";width:3px;height:3px;background:var(--green);border-radius:50%}
.story{display:flex;gap:6px;margin-bottom:6px}
.story .av{width:26px;height:26px;flex:none;border-radius:2px}
.story b{display:block;font-size:7px;color:var(--green);font-weight:600}
.story small{font-size:6px;color:var(--muted)}
.tabs{display:flex;margin-bottom:5px}
.tabs span{flex:1;font-size:6.5px;padding:3px 5px;border:1px solid var(--line);color:var(--muted)}
.tabs span.on{background:var(--green);color:var(--white);border-color:var(--green)}
.talk p{font-size:6.5px;margin-bottom:3px}
.players{display:grid;grid-template-columns:repeat(6,1fr);gap:4px}
.players span{height:24px;border-radius:2px}
.tags{display:flex;flex-wrap:wrap;gap:4px}
.tags span{font-size:6px;padding:2px 6px 2px 10px;background:var(--bg);border:1px solid var(--line);position:relative}
.tags span::before{content:"";position:absolute;left:3px;top:5px;width:4px;height:4px;background:var(--green);border-radius:50%}
.tags span.on{background:var(--green);color:var(--white);border-color:var(--green)}
.tags span.on::before{background:var(--white)}

/* footer */
.site-footer{position:absolute;left:0;top:1118px;width:756px;height:66px;background:var(--footer);color:#bbb;display:flex;gap:24px;padding:7px 30px}
.site-footer h5{font-size:9px;color:var(--white);font-weight:600;margin-bottom:4px}
.f-about{width:210px}
.f-about .row{display:flex;gap:6px}
.f-about .pic{width:34px;height:34px;flex:none;border-radius:2px}
.f-about p,.f-news p,.tweet{font-size:6px;line-height:1.4}
.f-news{width:230px}
.signup{display:flex;margin-top:4px}
.signup span{flex:1;height:13px;background:var(--white);font-size:6px;color:var(--muted);padding:2px 5px}
.signup b{background:var(--green);color:var(--white);font-size:6px;padding:3px 7px}
.f-tweets{flex:1}
.tweet{display:flex;gap:4px;margin-bottom:3px}
.tweet i{width:6px;height:6px;border-radius:50%;background:var(--green);flex:none;margin-top:2px}
.tweet em{color:var(--green);font-style:normal}
.f-social{display:flex;gap:4px}
.f-social span{width:9px;height:9px;border-radius:50%;background:#555}
.footer-bar{position:absolute;left:0;top:1184px;width:756px;height:16px;background:var(--footer-bar);color:#999;font-size:6px;display:flex;align-items:center;padding:0 30px;gap:12px}
.footer-bar .links{color:var(--green)}
</style>
</head>
<body>

<header class="site-header">
  <a class="brand" href="#"><span class="brand-dot"></span><span class="brand-name">Sideline Chatter</span></a>
  <div class="follow">Follow us :
    <span class="ico"></span><span class="ico"></span><span class="ico"></span><span class="ico g"></span><span class="ico"></span>
  </div>
  <nav class="nav">
    <a href="#">Home</a>
    <a href="#">World Cup</a>
    <a href="#">Teams <span class="caret">▼</span></a>
    <a href="#">Standings <span class="caret">▼</span></a>
    <a href="#" class="active">Blog ▾</a>
    <a href="#">Subscribe</a>
  </nav>
</header>

<section class="slider">
  <div class="tile"><div class="fill" role="img" aria-label="Photo of a player in the stadium" style="background:linear-gradient(160deg,#6a8a5a,#2c3b2a)"></div>
    <div class="caption"><span class="tag-label">Latest</span><h3>Corrupti quos</h3></div></div>
  <div class="tile"><div class="fill" role="img" aria-label="Photo of fans in yellow shirts" style="background:linear-gradient(160deg,#e3c53a,#5d6a2b)"></div>
    <div class="caption"><span class="tag-label">Inspecting</span><h3>Corrupti quos dolores</h3></div></div>
  <div class="tile big"><div class="fill" role="img" aria-label="Photo of the team celebrating on the pitch" style="background:linear-gradient(170deg,#8c9a8e 0%,#dcdcdc 45%,#3d5c34 100%)"></div>
    <div class="caption"><span class="tag-label">Inspecting</span><h3>Corrupti quos dolores eiquas</h3></div></div>
  <div class="tile"><div class="fill" role="img" aria-label="Photo of supporters with flags" style="background:linear-gradient(160deg,#d9b235,#1f6b3d)"></div>
    <div class="caption"><span class="tag-label">Inspecting</span><h3>Corrupti quos dolores</h3></div></div>
  <div class="tile"><div class="fill" role="img" aria-label="Photo of fans in the stands" style="background:linear-gradient(160deg,#f0d64a,#2e8a3f)"></div>
    <div class="caption"><span class="tag-label">Inspecting</span><h3>Corrupti quos dolores</h3></div></div>
  <div class="tile"><div class="fill" role="img" aria-label="Photo of a match moment" style="background:linear-gradient(160deg,#4c6a3c,#1f2b1c)"></div>
    <div class="caption"><span class="tag-label">Latest</span><h3>Corrupti quos</h3></div></div>
  <div class="tile"><div class="fill" role="img" aria-label="Photo of a player in red kit" style="background:linear-gradient(160deg,#b8453c,#3a3a3a)"></div>
    <div class="caption"><span class="tag-label">Inspecting</span><h3>Corrupti quos dolores</h3></div></div>
  <div class="tile"><div class="fill" role="img" aria-label="Photo of a goal celebration" style="background:linear-gradient(160deg,#5f8d4e,#9aa89a)"></div>
    <div class="caption"><span class="tag-label">Inspecting</span><h3>Corrupti quos dolores</h3></div></div>
  <div class="tile"><div class="fill" role="img" aria-label="Photo of cheering supporters" style="background:linear-gradient(160deg,#e8c63e,#b5473a)"></div>
    <div class="caption"><span class="tag-label">Inspecting</span><h3>Corrupti quos dolores</h3></div></div>
</section>
<div class="slider-band"></div>

<main class="content">
  <div class="posts">
    <article class="post">
      <div class="thumb" role="img" aria-label="Photo of players on the pitch" style="background:linear-gradient(150deg,#8fb2d6,#3f6a3a)"></div>
      <div>
        <h2>Corrupti quos dolores eiquas</h2>
        <div class="meta"><span><i></i>20 May 2014</span><span><i></i>12</span><span><i></i>Stadiums, Matchdays, Lumen League</span></div>
        <p>At vero eos et accusamus et iusto odio dignissimos ducimus qui blanditiis praesentium voluptatum deleniti atque corrupti quos dolores et quas molestias excepturi sint occaecati cupiditate non provident, similique sunt in culpa.</p>
        <p>Et harum quidem rerum facilis est et expedita distinctio nam libero tempore soluta nobis.</p>
        <a class="read-more" href="#">Read more »</a>
      </div>
    </article>
    <article class="post">
      <div class="thumb" role="img" aria-label="Photo of a crowd of fans" style="background:linear-gradient(150deg,#6a9ccf,#d9d9d9)"></div>
      <div>
        <h2>Corrupti quos dolores eiquas</h2>
        <div class="meta"><span><i></i>18 May 2014</span><span><i></i>8</span><span><i></i>Stadiums, Matchdays, Lumen League</span></div>
        <p>At vero eos et accusamus et iusto odio dignissimos ducimus qui blanditiis praesentium voluptatum deleniti atque corrupti quos dolores et quas molestias excepturi sint occaecati cupiditate non provident, similique sunt in culpa.</p>
        <p>Et harum quidem rerum facilis est et expedita distinctio nam libero tempore soluta nobis.</p>
        <a class="read-more" href="#">Read more »</a>
      </div>
    </article>
    <article class="post">
      <div class="thumb" role="img" aria-label="Photo of a player with the ball" style="background:linear-gradient(150deg,#c9c9c9,#3e6c34)"></div>
      <div>
        <h2>Corrupti quos dolores eiquas</h2>
        <div class="meta"><span><i></i>15 May 2014</span><span><i></i>5</span><span><i></i>Stadiums, Matchdays, Lumen League</span></div>
        <p>At vero eos et accusamus et iusto odio dignissimos ducimus qui blanditiis praesentium voluptatum deleniti atque corrupti quos dolores et quas molestias excepturi sint occaecati cupiditate non provident, similique sunt in culpa.</p>
        <p>Et harum quidem rerum facilis est et expedita distinctio nam libero tempore soluta nobis.</p>
        <a class="read-more" href="#">Read more »</a>
      </div>
    </article>
    <article class="post">
      <div class="thumb" role="img" aria-label="Photo of supporters with painted flags" style="background:linear-gradient(150deg,#e6c23c,#b8453a)"></div>
      <div>
        <h2>Corrupti quos dolores eiquas</h2>
        <div class="meta"><span><i></i>11 May 2014</span><span><i></i>3</span><span><i></i>Stadiums, Matchdays, Lumen League</span></div>
        <p>At vero eos et accusamus et iusto odio dignissimos ducimus qui blanditiis praesentium voluptatum deleniti atque corrupti quos dolores et quas molestias excepturi sint occaecati cupiditate non provident, similique sunt in culpa.</p>
        <p>Et harum quidem rerum facilis est et expedita distinctio nam libero tempore soluta nobis.</p>
        <a class="read-more" href="#">Read more »</a>
      </div>
    </article>
    <nav class="pagination">
      <a href="#">Prev</a><a href="#" class="current">1</a><a href="#">2</a><a href="#">3</a><a href="#">4</a><a href="#">5</a><a href="#">Next</a>
    </nav>
  </div>

  <aside class="sidebar">
    <section class="widget">
      <h4>Categories</h4>
      <ul class="cat-list">
        <li>Top Banter</li><li>Latest News (6)</li><li>Liga Champions Cup (3)</li><li>Players Updates (4)</li><li>World Finals 2014 (5)</li>
      </ul>
    </section>
    <section class="widget">
      <h4>Top Stories</h4>
      <div class="story"><span class="av" role="img" aria-label="Story thumbnail photo" style="background:#8aa878"></span><div><b>Fearless goalkeepers</b><small>June 12, 2014 · Amet dolor sit</small></div></div>
      <div class="story"><span class="av" role="img" aria-label="Story thumbnail photo" style="background:#c9a842"></span><div><b>Midfield masters</b><small>June 10, 2014 · Amet dolor sit</small></div></div>
      <div class="story"><span class="av" role="img" aria-label="Story thumbnail photo" style="background:#6f8fb5"></span><div><b>Derby day drama</b><small>June 08, 2014 · Amet dolor sit</small></div></div>
    </section>
    <section class="widget">
      <h4>Popular Talks</h4>
      <div class="tabs"><span class="on">Most Popular</span><span>Latest Comments</span></div>
      <div class="talk">
        <p>Nam libero tempore cum soluta nobis est eligendi optio cumque nihil impedit quo minus id quod maxime.</p>
        <p>Temporibus autem quibusdam et aut officiis debitis rerum necessitatibus saepe eveniet.</p>
      </div>
    </section>
    <section class="widget">
      <h4>Popular Football Players</h4>
      <div class="players" role="img" aria-label="Grid of player portrait photos">
        <span style="background:#a08a6c"></span><span style="background:#7b8f6a"></span><span style="background:#c2a27c"></span><span style="background:#6e7d8f"></span><span style="background:#b58f6a"></span><span style="background:#8a9a7c"></span>
        <span style="background:#9c7f62"></span><span style="background:#c6ad8a"></span><span style="background:#728a68"></span><span style="background:#a5886b"></span><span style="background:#8d98a6"></span><span style="background:#b89a78"></span>
      </div>
    </section>
    <section class="widget">
      <h4>Tags</h4>
      <div class="tags">
        <span>Finals</span><span>World Cup</span><span>Teams</span><span>Brazil</span><span>Goals</span><span>Transfers</span><span class="on">Prime Division</span><span>Players</span>
      </div>
    </section>
  </aside>
</main>

<footer class="site-footer">
  <div class="f-about">
    <h5>About</h5>
    <div class="row">
      <span class="pic" role="img" aria-label="Photo of a football on grass" style="background:linear-gradient(150deg,#5c9a4a,#2b5a2a)"></span>
      <p>Sideline Chatter brings you fresh match talk, team news and honest banter from every league, written by fans for fans.</p>
    </div>
  </div>
  <div class="f-news">
    <h5>Subscribe to our Newsletter</h5>
    <p>Subscribe to our newsletter and stay up to date with the latest news and deals!</p>
    <div class="signup"><span>Your email address</span><b>SUBSCRIBE</b></div>
  </div>
  <div class="f-tweets">
    <h5>Latest Tweets</h5>
    <div class="tweet"><i></i><span><em>@sidelinechat</em> Match day preview is live now, read our thoughts on the derby.</span></div>
    <div class="tweet"><i></i><span><em>@sidelinechat</em> New player ratings posted for the weekend, join the debate.</span></div>
    <div class="f-social"><span></span><span></span><span></span><span></span><span></span><span></span><span></span></div>
  </div>
</footer>
<div class="footer-bar"><span>2014 © Sideline Chatter. All Rights Reserved.</span><span class="links">Privacy Policy | Terms of Service</span></div>

</body>
</html>
```